Wordpress Lifestyle Blog

Just to be clear - I have the domain and the wordpress site (which is messy). I need someone to help me complete a simple blog design and then go into the existing wordpress site, and get rid of all the existing rubbish and set up the templates please. If we progress with design can we please be clear about additional costs upfront which, of course, I appreciate is the case.

Need a lifestyle blog. It is called brightyearsahead.com. Aimed at the older woman but needs to look fresh and young, not old fashioned. Navigation will be Home, Fashion, Feelings, Fitness, Contact. I have a logo but not sure it will work at the moment so happy with stylised words.Will have social media links.

Need homepage (not overly long) to have a main slider for pics/videos. Then the three category boxes underneath linking through to 2nd level pages containing blogs for that category and then the actual blog page. Happy to be led by expertise if this is not gonna work.

Am really looking for something clean and fresh like a Marwyn type approach to be honest.

If you need any further direction please just ask - once design chosen I am looking to move quickly.

Thank you so much for looking at this brief

Target Market(s)

Women, 40 - 60 age group but with a younger outlook

Number of Pages Required

3 page

Colors

Designer to choose colors to be used in the design.

Requirements
Must have
• Reflect youth, fun, bright
• Lift easily into a wordpress format
Should not have
• Old, staid, frumpy,dark

```html
<!DOCTYPE html>
<html lang="en">
<head>
<meta charset="utf-8">
<title>brightyearsahead — Follow</title>
<link href="https://fonts.googleapis.com/css2?family=Kaushan+Script&display=swap" rel="stylesheet">
<style>
:root{
  --blue:#0a0aee;
  --blue-deep:#0b14d8;
  --violet:#5452fb;
  --orange:#ef8a12;
  --white:#ffffff;
  --script:"Kaushan Script", cursive;
}
*{box-sizing:border-box;margin:0;padding:0}
html,body{width:1200px;height:1200px;overflow:hidden;background:var(--white)}
body{position:relative;font-family:var(--script)}
.abs{position:absolute}
.photo{position:absolute}
.top-strip .p1{left:0;top:0;width:298px;height:131px;background:linear-gradient(135deg,#8c90a8,#5c67b8 60%,#3c4aa0)}
.top-strip .p2{left:298px;top:0;width:601px;height:131px;background:linear-gradient(180deg,#6f6a70,#e8b39a 45%,#f2c3ab 70%,#8c8fa0)}
.top-strip .p3{left:899px;top:0;width:301px;height:131px;background:linear-gradient(90deg,#fbba1c,#f5b320 40%,#6e4a3c 55%,#f8b51e 75%)}
.load-more{left:487px;top:154px;width:225px;height:60px;background:var(--blue);color:var(--white);font-size:20px;display:flex;align-items:center;justify-content:center;letter-spacing:.5px}
.rule{height:1.5px;background:var(--orange)}
.section-title{width:1200px;left:0;text-align:center;color:var(--blue-deep);font-size:38px;line-height:1}
.handle{width:1200px;left:0;text-align:center;color:var(--orange);font-size:25px}
.col-title{color:var(--orange);font-size:26px;text-align:center;width:300px}
.panel{background:var(--violet);color:var(--white);width:277px;height:224px}
.subscribe-here{left:150px;top:406px;display:flex;flex-direction:column;align-items:center;justify-content:center;font-size:50px;line-height:1.05;text-align:center}
.inbox{left:773px;top:406px}
.inbox .lede{position:absolute;left:0;top:60px;width:277px;text-align:center;font-size:12.5px}
.inbox .field{position:absolute;left:38px;top:96px;width:203px;height:29px;background:var(--white)}
.inbox .send{position:absolute;left:91px;top:146px;width:97px;height:30px;background:var(--white);color:var(--violet);font-size:14px;display:flex;align-items:center;justify-content:center}
.social{width:72px;height:72px;border-radius:50%;display:flex;align-items:center;justify-content:center;color:var(--white);font-size:12px;text-align:center}
.s-a{background:radial-gradient(circle,#6f88c8,#8496cc)}
.s-b{background:radial-gradient(circle,#5cb4e6,#7cc6ec)}
.s-c{background:radial-gradient(circle,#b68ac8,#e6b27a)}
.s-d{background:radial-gradient(circle,#ec6a4c,#f08a6c)}
.s-e{background:radial-gradient(circle,#5ab0e0,#86c4ea)}
.s-f{background:radial-gradient(circle,#d85a3c,#e87a5c)}
.insta .q1{left:0;top:830px;width:225px;height:300px;background:linear-gradient(135deg,#f2f2f2,#3f4a62 50%,#eceae6)}
.insta .q2{left:225px;top:830px;width:224px;height:300px;background:linear-gradient(180deg,#8a8476,#e8e2d8 50%,#2e5a62)}
.insta .q3{left:449px;top:830px;width:300px;height:300px;background:linear-gradient(160deg,#c9d4e4,#8a6a62 40%,#eef0f4)}
.insta .q4{left:749px;top:830px;width:226px;height:300px;background:linear-gradient(135deg,#f0e6dc,#e8d8c8 50%,#b87858)}
.insta .q5{left:975px;top:830px;width:225px;height:300px;background:linear-gradient(180deg,#9ccccc,#f0c040 55%,#7aa0c8)}
.footer{left:0;top:1130px;width:1200px;height:70px;background:var(--orange);color:var(--white);font-size:14px}
.footer .copy{position:absolute;left:150px;top:22px}
.footer .legal{position:absolute;right:153px;top:22px}
</style>
</head>
<body>
<div class="top-strip">
  <div class="photo p1" role="img" aria-label="Woman in a blue top looking at her phone"></div>
  <div class="photo p2" role="img" aria-label="Peach ruffled gown trailing across a wooden deck"></div>
  <div class="photo p3" role="img" aria-label="Woman in a checked skirt against a yellow wall"></div>
</div>

<div class="abs load-more">LOAD MORE</div>

<div class="abs rule" style="left:0;top:315px;width:505px"></div>
<div class="abs rule" style="left:695px;top:315px;width:505px"></div>
<h2 class="abs section-title" style="top:296px">Follow Me</h2>

<h3 class="abs col-title" style="left:139px;top:360px">Join My Newsletter</h3>
<div class="abs panel subscribe-here"><span>Subscribe</span><span>here</span></div>

<div class="abs social s-a" style="left:473px;top:424px">Friendly</div>
<div class="abs social s-b" style="left:565px;top:424px">Chirper</div>
<div class="abs social s-c" style="left:656px;top:424px">Photofeed</div>
<div class="abs social s-d" style="left:473px;top:534px">Pinboard</div>
<div class="abs social s-e" style="left:572px;top:534px">Linkwork</div>
<div class="abs social s-f" style="left:656px;top:534px">Viewtube</div>

<h3 class="abs col-title" style="left:762px;top:360px">Don’t Miss a Post</h3>
<div class="abs panel inbox">
  <p class="lede">Get every post delivered to your inbox</p>
  <div class="field"></div>
  <div class="send">SUBSCRIBE</div>
</div>

<div class="abs rule" style="left:0;top:739px;width:490px"></div>
<div class="abs rule" style="left:706px;top:739px;width:494px"></div>
<h2 class="abs section-title" style="top:718px">Photofeed</h2>
<p class="abs handle" style="top:762px">@brightyearsahead</p>

<div class="insta">
  <div class="photo q1" role="img" aria-label="Folded jeans, white knit sweater and glasses"></div>
  <div class="photo q2" role="img" aria-label="Woman in a sun hat sitting on seaside rocks"></div>
  <div class="photo q3" role="img" aria-label="Makeup brushes in white lace cups"></div>
  <div class="photo q4" role="img" aria-label="Woman browsing heels in a shoe shop"></div>
  <div class="photo q5" role="img" aria-label="Woman in sunglasses and a yellow shirt against a teal wall"></div>
</div>

<footer class="abs footer">
  <span class="copy">Copyright © 2018 brightyearsahead | All Rights Reserved</span>
  <span class="legal">Privacy Policy | Terms &amp; Conditions</span>
</footer>
</body>
</html>
```